Design a upcoming mobile game webpage

I have a domain space up but as I am still needed to work on getting the content and every other things setup, I would like to at least populate the page with a coming soon page with videos/images or links to plenvo,qk etc and a newsletter sign up.
It can be design as a full game site but to illustrate it as "Coming soon to you on ZUL and Velmora"
Target Market(s)
Consumer who holds a mobile device
Industry/Entity Type
Velmora

```html
<!DOCTYPE html>
<html lang="en">
<head>
<meta charset="utf-8">
<title>Mythborne is coming soon</title>
<link rel="stylesheet" href="https://fonts.googleapis.com/css2?family=Ubuntu:wght@300;400;500;700&family=Roboto+Condensed:wght@400;700&display=swap">
<style>
  :root {
    --accent: #38a6ee;
    --white: #ffffff;
    --bar: #2d3138;
    --ink-dark: #141414;
    --ink-mid: #5e5e5e;
    --ink-light: #a9a9a9;
    --frame: rgba(255,255,255,0.85);
    --muted: #e6e6e6;
  }
  * { box-sizing: border-box; margin: 0; padding: 0; }
  html, body { width: 1200px; height: 913px; overflow: hidden; }
  body {
    position: relative;
    font-family: "Ubuntu", sans-serif;
    color: var(--white);
    background: var(--ink-dark);
  }
  .hero-backdrop {
    position: absolute; inset: 0;
    background:
      radial-gradient(ellipse 320px 520px at 600px 430px, rgba(20,20,20,0.85), transparent 70%),
      radial-gradient(ellipse 700px 260px at 600px 860px, #6f6f6f, transparent 75%),
      radial-gradient(ellipse 500px 300px at 250px 250px, #9a9a9a, transparent 70%),
      radial-gradient(ellipse 500px 300px at 950px 200px, #7d7d7d, transparent 70%),
      linear-gradient(180deg, var(--ink-light) 0%, var(--ink-mid) 45%, #2a2a2a 75%, #4a4a4a 100%);
  }
  .social-bar {
    position: absolute; left: 143px; top: 22px; width: 914px; height: 68px;
    background: var(--bar); border-radius: 3px;
    display: flex; justify-content: space-around; align-items: center;
    list-style: none;
  }
  .social-bar li { font-size: 15px; font-weight: 500; color: var(--white); }
  .headline {
    position: absolute; top: 138px; left: 0; width: 1200px; text-align: center;
    font-size: 57px; font-weight: 500; letter-spacing: -0.5px;
  }
  .accent { color: var(--accent); }
  .countdown-label {
    position: absolute; top: 252px; width: 1200px; text-align: center;
    font-size: 45px; font-weight: 300;
  }
  .countdown {
    position: absolute; left: 158px; top: 335px; width: 885px; height: 167px;
    border: 1px solid var(--frame); border-radius: 18px;
    display: flex; align-items: center; justify-content: center;
    font-size: 124px; font-weight: 300; letter-spacing: 1px;
  }
  .newsletter-title {
    position: absolute; top: 572px; width: 1200px; text-align: center;
    font-size: 45px; font-weight: 400;
  }
  .newsletter-text {
    position: absolute; top: 646px; width: 1200px; text-align: center;
    font-size: 16px; font-weight: 300; color: var(--muted);
  }
  .signup { position: absolute; left: 158px; top: 706px; width: 879px; height: 44px; }
  .signup-input {
    position: absolute; left: 0; top: 0; width: 601px; height: 40px;
    border: 0; border-bottom: 1px solid rgba(255,255,255,0.4);
    border-left: 2px solid var(--accent);
    background: rgba(0,0,0,0.15);
    padding-left: 16px; font-family: "Ubuntu", sans-serif; font-size: 16px;
    color: var(--white);
  }
  .signup-input::placeholder { color: rgba(255,255,255,0.55); }
  .signup-button {
    position: absolute; left: 603px; top: 0; width: 276px; height: 44px;
    border: 0; background: var(--accent); color: var(--white);
    font-family: "Ubuntu", sans-serif; font-size: 23px;
  }
  .site-footer {
    position: absolute; top: 818px; width: 1200px; text-align: center;
    font-family: "Roboto Condensed", sans-serif; font-size: 17px; color: var(--muted);
  }
</style>
</head>
<body>
  <div class="hero-backdrop" role="img" aria-label="Dark monochrome photo of a warrior standing on a heap of skulls under a stormy sky"></div>

  <ul class="social-bar">
    <li>Stackly</li>
    <li>Vidora</li>
    <li>Linkwell</li>
    <li>Pinora</li>
    <li>qk</li>
    <li>plenvo</li>
  </ul>

  <h1 class="headline"><span class="accent">Mythborne</span> is comming <span class="accent">soon</span></h1>

  <h2 class="countdown-label">We go live in:</h2>
  <div class="countdown">23:02:54:37</div>

  <h2 class="newsletter-title">Subscribe to <span class="accent">our newsletter</span></h2>
  <p class="newsletter-text">Sign up now to our newsletter and you'll be one of the first to know when the site is ready:</p>

  <form class="signup">
    <input class="signup-input" type="email" placeholder="Enter Email">
    <button class="signup-button" type="button">Subscribe</button>
  </form>

  <footer class="site-footer">© 2014 <span class="accent">Mythborne</span>. All Rights Reserved.</footer>
</body>
</html>
```